Redesign Comparisson chart - make modern and effective

Use your imaginations to make a powerful distinction between KRV & other holistic modalities. There are 7 elements physical, mental, emotional, energetic, subconscious, superconscious and before and after testing.
We want it to be obvious that KRV is the only modality that works on all these elements simultaneously. We do not want to include any chakras as we want this information to be accepted by a wide range of people and belief systems.'

We want it to look simple but effective. Professional but powerful. We want KRV to stand out even of you eye just passed over i.
Updates

Hi everyone, thanks for your submissions so far. Basically what this image is meant to represent is a comparison chart between all the modalities There are 5 elements physical, mental, emotional, subconscious and superconscious. we want to reflect that KRV is the only modality that works on all these elements simultaneously. As we want the concept to be accepted and not considered woo woo, we want to steer away from chakras.

Target Market(s)

Professionals

Industry/Entity Type

Professional services

Font styles to use
Sans Serif
Other font styles liked:
• Poppins Monserratt

Colors
0094D4
00A9DD
6FCCEA
C7EBF8
E9F6FB

Requirements
Must have
• Clear/professional and clean look. Brand colours and logos. All typography and formats must be cohesive.
Nice to have
• More easy to read, different layout
Should not have
• Do not change the data just the way its presented. No chakras

```html
<!DOCTYPE html>
<html lang="en">
<head>
<meta charset="utf-8">
<title>KRV Modality Comparison Chart</title>
<link href="https://fonts.googleapis.com/css2?family=Poppins:wght@400;500;600;700;800&display=swap" rel="stylesheet">
<style>
:root{
  --brand-deep:#0094D4;
  --brand:#00A9DD;
  --brand-mid:#6FCCEA;
  --brand-pale:#C7EBF8;
  --brand-mist:#E9F6FB;
  --stripe:#1BB1E2;
  --physical:#FF3A00;
  --mental:#0094D4;
  --emotional:#8CC63F;
  --energetic:#FBAF3F;
  --subconscious:#F5E82F;
  --superconscious:#6B2A8E;
  --testing:#C6168D;
  --ink:#333;
  --muted:#666;
}
*{margin:0;padding:0;box-sizing:border-box}
html,body{width:873px;height:1200px;overflow:hidden;background:#fff}
body{font-family:"Poppins",sans-serif;position:relative;color:var(--ink)}
.headline{position:absolute;left:320px;width:510px;top:54px;text-align:center;color:var(--brand-deep);font-weight:800;font-size:17.5px;letter-spacing:-.2px}
.intro{position:absolute;left:318px;width:514px;top:76px;text-align:center;color:var(--muted);font-size:10.6px;line-height:13px}
.band{position:absolute;left:0;top:125px;width:873px;height:798px;background:var(--brand-pale)}
.panel{position:absolute;left:90px;top:125px;width:748px;height:798px;background:var(--brand);border-radius:10px}
.brand-box{position:absolute;left:110px;top:89px;width:169px;height:71px;background:#fff;border:2px solid var(--brand);border-radius:4px;display:flex;align-items:center;gap:8px;padding-left:11px}
.brand-dot{width:55px;height:55px;border-radius:50%;background:var(--brand);flex:none}
.brand-name{color:var(--brand);font-weight:700;font-size:16px;line-height:16px}
.chart{position:absolute;left:90px;top:135px;width:731px}
.row{display:grid;grid-template-columns:217px repeat(7,73.5px);position:relative}
.row.alt .label{background:var(--stripe)}
.label{color:#fff;font-size:12px;line-height:17.5px;padding-left:20px;display:flex;flex-direction:column;justify-content:center;text-transform:uppercase}
.cell{border-right:1px solid var(--brand-mid);border-bottom:1px solid var(--brand-mid);display:flex;align-items:center;justify-content:center}
.cell:nth-child(2){border-left:1px solid var(--brand-mid)}
.head .label{background:none}
.head .cell{border:none;margin-right:1px;font-size:8.4px;line-height:10px;text-align:center;color:#fff;height:28px;flex-direction:column}
.head{margin-bottom:1px}
.h-physical{background:var(--physical)}
.h-mental{background:#fff;color:var(--brand-deep)!important}
.h-emotional{background:var(--emotional)}
.h-energetic{background:var(--energetic)}
.h-sub{background:var(--subconscious);color:var(--brand-deep)!important}
.h-super{background:var(--superconscious)}
.h-testing{background:var(--testing)}
.star{width:22px;height:22px}
.star use{stroke:#fff;stroke-width:2.2}
.star.outline use{fill:var(--brand);}
.c-p{color:var(--physical)}.c-m{color:var(--mental)}.c-e{color:var(--emotional)}.c-n{color:var(--energetic)}.c-s{color:var(--subconscious)}.c-u{color:var(--superconscious)}.c-t{color:var(--testing)}
.feature{z-index:1}
.feature::before{content:"";position:absolute;left:-40px;right:-30px;top:0;bottom:0;background:#B4E3F4;border:1.5px solid var(--brand-deep);border-radius:3px;box-shadow:0 3px 5px rgba(0,60,100,.35);z-index:-1}
.feature .label{flex-direction:row;align-items:center;justify-content:flex-start;gap:10px;padding-left:20px}
.feature .cell{border-color:rgba(111,204,234,.6)}
.feature-dot{width:31px;height:31px;border-radius:50%;background:var(--brand);flex:none}
.feature-name{color:var(--brand);font-weight:800;font-size:11px;line-height:11px}
.feature .star{width:30px;height:30px}
.feature .star use{stroke:none}
.notes{position:absolute;top:937px;width:168px;font-size:9px;line-height:10.5px;text-align:justify;color:#222}
.notes h3{display:inline;font-size:10.5px;font-weight:600;margin-right:6px}
.notes p+p{margin-top:12px}
</style>
</head>
<body>
<svg width="0" height="0" style="position:absolute">
  <defs>
    <symbol id="star" viewBox="0 0 40 40"><path d="M20 2 L24.5 15.5 L38 20 L24.5 24.5 L20 38 L15.5 24.5 L2 20 L15.5 15.5Z" fill="currentColor"/></symbol>
  </defs>
</svg>

<h1 class="headline">Choose KRV For Fast, Immediate and Powerful Results.</h1>
<p class="intro">I must experience healing on all levels I am not just a body I want to learn how to heal myself so i'm not dependent on others. I want to release all my emotional and mental blocks so I can be the best version of myself.</p>

<div class="band"></div>
<div class="panel"></div>

<div class="brand-box"><span class="brand-dot"></span><span class="brand-name">kindred<br>root<br>vitality</span></div>

<div class="chart">
  <div class="row head"><div class="label"></div>
    <div class="cell h-physical">PHYSICAL</div><div class="cell h-mental">MENTAL</div><div class="cell h-emotional">EMOTIONAL</div><div class="cell h-energetic">ENERGETIC</div><div class="cell h-sub">SUB<br>CONSCIOUS</div><div class="cell h-super">SUPER<br>CONSCIOUS</div><div class="cell h-testing">BEFORE &amp;<br>AFTER TESTING</div>
  </div>

  <div class="row" style="height:106px"><div class="label"><span>Massage</span><span>Yoga</span><span>Natropathy</span><span>Ayurvedic Medicine</span><span>Western Medicine</span></div>
    <div class="cell"><svg class="star c-p"><use href="#star"/></svg></div><div class="cell"></div><div class="cell"></div><div class="cell"></div><div class="cell"></div><div class="cell"></div><div class="cell"></div></div>

  <div class="row alt" style="height:34px"><div class="label">Psychic Intuitive</div>
    <div class="cell"><svg class="star c-p"><use href="#star"/></svg></div><div class="cell"><svg class="star outline"><use href="#star"/></svg></div><div class="cell"></div><div class="cell"></div><div class="cell"></div><div class="cell"></div><div class="cell"></div></div>

  <div class="row" style="height:36px"><div class="label">Family Constellation</div>
    <div class="cell"><svg class="star c-p"><use href="#star"/></svg></div><div class="cell"><svg class="star outline"><use href="#star"/></svg></div><div class="cell"></div><div class="cell"><svg class="star c-n"><use href="#star"/></svg></div><div class="cell"></div><div class="cell"></div><div class="cell"></div></div>

  <div class="row alt" style="height:34px"><div class="label">Acupuncture</div>
    <div class="cell"><svg class="star c-p"><use href="#star"/></svg></div><div class="cell"></div><div class="cell"></div><div class="cell"><svg class="star c-n"><use href="#star"/></svg></div><div class="cell"></div><div class="cell"></div><div class="cell"></div></div>

  <div class="row" style="height:37px"><div class="label">Nutritional Healing</div>
    <div class="cell"><svg class="star c-p"><use href="#star"/></svg></div><div class="cell"></div><div class="cell"></div><div class="cell"></div><div class="cell"></div><div class="cell"></div><div class="cell"><svg class="star c-t"><use href="#star"/></svg></div></div>

  <div class="row alt" style="height:34px"><div class="label">Chinese Medicine</div>
    <div class="cell"><svg class="star c-p"><use href="#star"/></svg></div><div class="cell"></div><div class="cell"></div><div class="cell"><svg class="star c-n"><use href="#star"/></svg></div><div class="cell"></div><div class="cell"></div><div class="cell"><svg class="star c-t"><use href="#star"/></svg></div></div>

  <div class="row" style="height:49px"><div class="label"><span>Kinesiology</span><span>Bowen Therapy</span></div>
    <div class="cell"><svg class="star c-p"><use href="#star"/></svg></div><div class="cell"></div><div class="cell"></div><div class="cell"></div><div class="cell"><svg class="star c-s"><use href="#star"/></svg></div><div class="cell"></div><div class="cell"><svg class="star c-t"><use href="#star"/></svg></div></div>

  <div class="row feature" style="height:42px"><div class="label"><span class="feature-dot"></span><span class="feature-name">KINDRED ROOT<br>VITALITY</span></div>
    <div class="cell"><svg class="star c-p"><use href="#star"/></svg></div><div class="cell"><svg class="star c-m"><use href="#star"/></svg></div><div class="cell"><svg class="star c-e"><use href="#star"/></svg></div><div class="cell"><svg class="star c-n"><use href="#star"/></svg></div><div class="cell"><svg class="star c-s"><use href="#star"/></svg></div><div class="cell"><svg class="star c-u"><use href="#star"/></svg></div><div class="cell"><svg class="star c-t"><use href="#star"/></svg></div></div>

  <div class="row" style="height:33px"><div class="label">EFT</div>
    <div class="cell"><svg class="star c-p"><use href="#star"/></svg></div><div class="cell"><svg class="star outline"><use href="#star"/></svg></div><div class="cell"></div><div class="cell"></div><div class="cell"><svg class="star c-s"><use href="#star"/></svg></div><div class="cell"></div><div class="cell"><svg class="star c-t"><use href="#star"/></svg></div></div>

  <div class="row alt" style="height:34px"><div class="label">Chiropratic</div>
    <div class="cell"><svg class="star c-p"><use href="#star"/></svg></div><div class="cell"></div><div class="cell"></div><div class="cell"><svg class="star c-n"><use href="#star"/></svg></div><div class="cell"><svg class="star c-s"><use href="#star"/></svg></div><div class="cell"></div><div class="cell"><svg class="star c-t"><use href="#star"/></svg></div></div>

  <div class="row" style="height:48px"><div class="label"><span>Reiki</span><span>Crystal Healing</span></div>
    <div class="cell"></div><div class="cell"></div><div class="cell"></div><div class="cell"><svg class="star c-n"><use href="#star"/></svg></div><div class="cell"></div><div class="cell"></div><div class="cell"></div></div>

  <div class="row alt" style="height:35px"><div class="label">Energy Medicine</div>
    <div class="cell"></div><div class="cell"></div><div class="cell"></div><div class="cell"><svg class="star c-n"><use href="#star"/></svg></div><div class="cell"></div><div class="cell"></div><div class="cell"><svg class="star c-t"><use href="#star"/></svg></div></div>

  <div class="row" style="height:34px"><div class="label">Theta Healing</div>
    <div class="cell"></div><div class="cell"></div><div class="cell"></div><div class="cell"></div><div class="cell"><svg class="star c-s"><use href="#star"/></svg></div><div class="cell"><svg class="star c-u"><use href="#star"/></svg></div><div class="cell"></div></div>

  <div class="row alt" style="height:34px"><div class="label">Pshychology</div>
    <div class="cell"></div><div class="cell"><svg class="star outline"><use href="#star"/></svg></div><div class="cell"></div><div class="cell"></div><div class="cell"></div><div class="cell"></div><div class="cell"></div></div>

  <div class="row" style="height:54px"><div class="label"><span>Mindfullness Meditation</span><span>Life Coaching</span></div>
    <div class="cell"></div><div class="cell"><svg class="star outline"><use href="#star"/></svg></div><div class="cell"></div><div class="cell"></div><div class="cell"></div><div class="cell"></div><div class="cell"><svg class="star c-t"><use href="#star"/></svg></div></div>

  <div class="row alt" style="height:57px"><div class="label"><span>Hypnotherapy</span><span>Inner Child Healing</span></div>
    <div class="cell"></div><div class="cell"><svg class="star outline"><use href="#star"/></svg></div><div class="cell"></div><div class="cell"></div><div class="cell"><svg class="star c-s"><use href="#star"/></svg></div><div class="cell"></div><div class="cell"></div></div>

  <div class="row" style="height:41px"><div class="label"><span>NLP</span><span>Timeline Therapy</span></div>
    <div class="cell"></div><div class="cell"><svg class="star outline"><use href="#star"/></svg></div><div class="cell"></div><div class="cell"></div><div class="cell"><svg class="star c-s"><use href="#star"/></svg></div><div class="cell"></div><div class="cell"><svg class="star c-t"><use href="#star"/></svg></div></div>
</div>

<div class="notes" style="left:110px">
  <p><h3 style="color:var(--physical)">PHYSICAL</h3>dolor sit amet, consectetuer adipiscing elit, sed diam nonummy nibh euismod tincidunt ut laoreet dolore magna aliquam erat volutpat. Ut wisi enim ad minim veniam, quis nostrud exerci tation ullamcorper suscipit lobortis nisl ut aliquip ex ea commodo consequat. Duis autem vel eum iriure dolor in hendrerit in vulputate velit esse molestie consequat, vel illum dolore eu feugiat nulla facilisis at vero eros et accumsan et iusto odio dignissim qui blandit praesent luptatum zzril delenit augue duis dolore te feugait nulla facilisi. Lorem ipsum dolor sit amet, cons ectetuer adipiscing elit, sed diam nonummy nibh euismod tincidunt ut laoreet dolore magna aliquam erat volutpat. Ut wisi</p>
</div>
<div class="notes" style="left:291px">
  <p><h3 style="color:var(--mental)">MENTAL</h3>dolor sit amet, consectetuer adipiscing elit, sed diam nonummy nibh euismod tincidunt ut laoreet dolore magna aliquam erat volutpat. Ut wisi enim ad minim veniam, quis nostrud exerci tation ullamcorper suscipit lobortis nisl ut aliquip ex ea commodo consequat. Duis autem vel eum iriure dolor in hendrerit in vulputate velit esse molestie consequat, vel illum dolore eu feugiat nulla facilisis at.</p>
  <p><h3 style="color:var(--emotional)">EMOTIONAL</h3>dolor sit amet, consectetuer adipiscing elit, sed diam nonummy nibh euismod tincidunt ut laoreet dolore magna aliquam erat volutpat. Ut wisi enim ad minim veniam, quis nostrud exerci tation ullamcorper suscipit lobortis nisl ut aliquip ex ea commodo consequat.</p>
</div>
<div class="notes" style="left:472px">
  <p><h3 style="color:var(--energetic)">ENERGETIC</h3>dolor sit amet, consectetuer adipiscing elit, sed diam nonummy nibh euismod tincidunt ut laoreet dolore magna aliquam erat volutpat. Ut wisi enim ad minim veniam, quis nostrud exerci tation ullamcorper suscipit lobortis</p>
  <p style="margin-top:14px"><h3 style="color:var(--superconscious)">SUPER CONCSIOUS</h3>dolor sit amet, consectetuer adipiscing elit, sed diam nonummy nibh euismod tincidunt ut laoreet dolore magna aliquam erat volutpat. Ut wisi enim ad minim veniam, quis nostrud exerci tation ullamcorper suscipit lobortis laoreet dolore magna aliquam erat volutpat. Ut wisi enim ad minim veniam, quis nostrud exerci tation ullamcorper suscipit lo</p>
</div>
<div class="notes" style="left:654px">
  <p><h3 style="color:var(--subconscious)">SUB CONSCIOUS</h3>dolor sit amet, consectetuer adipiscing elit, sed diam nonummy nibh euismod tincidunt ut laoreet dolore magna aliquam erat volutpat. Ut wisi enim ad minim veniam, quis nostrud exerci tation ullamcorper suscipit lobortis nisl ut aliquip ex ea commodo consequat. Duis autem vel eum iriure dolor in hendrerit in vulputate velit esse molestie consequat, vel illum dolore eu feugiat nulla facilisis at.</p>
  <p><h3 style="color:var(--testing)">BEFORE AND AFTER TESTING</h3>dolor sit amet, consectetuer adipiscing elit, sed diam nonummy nibh euismod tincidunt ut laoreet dolore magna aliquam erat volutpat. Ut wisi enim ad minim veniam, quis nostrud exerci tation ullamcorper suscipit lobortis nisl ut aliquip ex ea commodo consequat.</p>
</div>
</body>
</html>
```